ZESTORAMA Business Card Design

ZESTORAMA
Zestorama is a food van, serving high vibe delicious food to go. This business is dedicated to healthy delicious feel good food, beauty in service and a sustainable planet.

The van will operate in the south west of western Australia at music festivals events markets wherever people need great food to go!

I like the idea of vibrant green mixed with a yellow?? background with some rays like the sun through the background.
The font needs to say vibrant energetic
TO ME -vibrant energetic font has to appear to be on the move - perhaps with shading??

I like fusha if that works for font? but the colour has to say food too.

I would like a symbol on the card a simple V turned into a womans raised arms. This should be vibrant too.
Thank you
Blessings
Marisol

Target Market(s)

target lovers of healthy high vibe food. music festival goers. age 18- 50 feel. audiance conscious eaters of feel great food

Industry/Entity Type

Events

Contact Information for Business Card

ZESTORAMA
High Vibe Food
Van
Marisol -owner/opperator
0417385960
Face book symbol - ZESTORAMA

on the I would like a logo of a simple V turned into a womans arms up toward the sky flip side

My number and name again
Zestorama- feel great mobile food
Festivals, events, markets & where high vibe food 2 go is appreciated

Requirements
Nice to have
• Moving energetic font
colour that says high vibe and healthy food

a logo that is a simple V turned into a woman's raised arms in gratitude

```html
<!DOCTYPE html>
<html lang="en">
<head>
<meta charset="utf-8">
<title>Zestorama Business Card</title>
<link href="https://fonts.googleapis.com/css2?family=Poppins:wght@500;700;800&display=swap" rel="stylesheet">
<style>
  :root {
    --bg: #e9e6df;
    --ray-light: #e6f03a;
    --ray-mid: #b8e02c;
    --ray-deep: #5cbf2a;
    --fuchsia: #e8127c;
    --fuchsia-soft: #ee3d93;
    --ink: #2a1020;
    --white: #ffffff;
  }
  * { box-sizing: border-box; margin: 0; padding: 0; }
  html, body { width: 1200px; height: 723px; overflow: hidden; }
  body {
    background: var(--bg);
    font-family: "Poppins", "Century Gothic", sans-serif;
    position: relative;
  }
  .card {
    position: absolute;
    top: 61px;
    width: 380px;
    height: 600px;
    border-radius: 6px;
    overflow: hidden;
    box-shadow: 0 6px 18px rgba(0,0,0,0.18);
    text-align: center;
  }
  .card--back { left: 170px; }
  .card--front { left: 650px; }
  .card__rays {
    position: absolute;
    inset: 0;
    background: radial-gradient(circle at 50% 38%, var(--ray-light) 0%, var(--ray-mid) 45%, var(--ray-deep) 100%);
  }
  .card__content {
    position: relative;
    height: 100%;
    padding: 34px 28px;
    display: flex;
    flex-direction: column;
    align-items: center;
  }
  .brand-name {
    color: var(--fuchsia);
    font-weight: 800;
    font-size: 44px;
    line-height: 1;
    letter-spacing: 0.5px;
  }
  .brand-circle {
    border-radius: 50%;
    background: var(--fuchsia);
  }
  .card--front .brand-circle { width: 150px; height: 150px; margin-bottom: 22px; }
  .card--back .brand-circle { width: 220px; height: 220px; margin: 28px 0 30px; }
  .tagline {
    color: var(--ink);
    font-weight: 700;
    font-size: 24px;
    margin-top: 8px;
  }
  .contact-name {
    color: var(--fuchsia);
    font-weight: 700;
    font-size: 24px;
    margin-top: 34px;
    line-height: 1.1;
  }
  .contact-role {
    color: var(--fuchsia-soft);
    font-weight: 500;
    font-size: 22px;
    line-height: 1.1;
  }
  .contact-phone {
    color: var(--fuchsia);
    font-weight: 700;
    font-size: 28px;
    margin-top: 6px;
  }
  .social {
    display: flex;
    align-items: center;
    gap: 10px;
    margin-top: 30px;
    color: var(--fuchsia);
    font-weight: 700;
    font-size: 24px;
  }
  .social__square {
    width: 28px;
    height: 28px;
    background: var(--fuchsia);
    border-radius: 4px;
  }
  .contact-email {
    color: var(--ink);
    font-weight: 500;
    font-size: 20px;
    margin-top: 10px;
  }
  .pitch {
    color: var(--fuchsia);
    font-weight: 700;
    font-size: 22px;
    line-height: 1.15;
    margin-top: 10px;
  }
  .dedication {
    color: var(--fuchsia);
    font-weight: 800;
    font-size: 28px;
    line-height: 1.1;
  }
</style>
</head>
<body>

  <section class="card card--back">
    <div class="card__rays" role="img" aria-label="Sunburst rays in yellow and green radiating from the centre"></div>
    <div class="card__content">
      <h1 class="brand-name">ZESTORAMA</h1>
      <p class="pitch">Food That Makes<br>You Feel Great at<br>festivals,<br>community events<br>&amp; private gatherings</p>
      <div class="brand-circle" role="img" aria-label="Zestorama brand mark"></div>
      <p class="dedication">Dedicated to<br>conscious, joyous<br>eating</p>
    </div>
  </section>

  <section class="card card--front">
    <div class="card__rays" role="img" aria-label="Sunburst rays in yellow and green radiating from the centre"></div>
    <div class="card__content">
      <div class="brand-circle" role="img" aria-label="Zestorama brand mark"></div>
      <h2 class="brand-name">ZESTORAMA</h2>
      <p class="tagline">High Vibe Food Van</p>
      <p class="contact-name">Marisol</p>
      <p class="contact-role">owner/operator</p>
      <p class="contact-phone">0417385960</p>
      <p class="social"><span class="social__square"></span>ZESTORAMA</p>
      <p class="contact-email">marisol@zestorama.com</p>
    </div>
  </section>

</body>
</html>
```